I want a website to be designed for our new company, it's an import and export company for variety of things.

please see the attached Logo for our company and the Images for our different sections for our busienss

Target Market(s)

multiple

Coding

Coded - Design and coding required

Number of Pages Required

5+ page

Font styles to use
Sans Serif

Colors

Designer to choose colors to be used in the design.

Requirements
Must have
• KDR WORLDWIDE
• KDR worlwide Supply & Building provides various services. The Company offers infrastructure construction, oil, enegy and gas services, agricultural projects, real estate development, travel and tourism, and food processing and trading.
• Civil contracting for infrastructure, residential and heavy projects. Through its main subsidiaries; distribution of general food products, construction chemicals including corrosion inhibitors and electrical machinery; provides catering and travel agency services; ownership and operation of a school; offers human sources services including manpower supply.
• Drilling and Gold Mines Used Machinery, All Kinds of Construction Machinery, Drilling Machines are manufactured and sold.
Nice to have
• good designa and beautiful colours, it has too look professional

```html
<!DOCTYPE html>
<html lang="en">
<head>
<meta charset="utf-8">
<title>KDR WORLDWIDE — Trading &amp; Contracting Services</title>
<link href="https://fonts.googleapis.com/css2?family=Roboto:wght@400;500;700;900&family=Roboto+Slab:wght@300;400&display=swap" rel="stylesheet">
<style>
:root{
  --accent:#c0822e;
  --ink:#1b1b1b;
  --black:#111111;
  --footer:#151515;
  --chair-bg:#f3eeee;
  --news-bg:#dcdcdc;
  --muted:#7b7b7b;
  --white:#ffffff;
  --body:#3a3a3a;
}
*{box-sizing:border-box;margin:0;padding:0}
html,body{width:1200px;height:4542px;overflow:hidden}
body{position:relative;font-family:"Roboto",sans-serif;color:var(--ink);background:var(--white)}
.abs{position:absolute}
.serif{font-family:"Roboto Slab",serif;font-weight:300}
.btn{position:absolute;background:var(--accent);color:var(--white);font-weight:700;text-transform:uppercase;display:flex;align-items:center;justify-content:center;letter-spacing:.5px}
.ornament{position:absolute;left:530px;width:140px;height:40px;border-radius:20px 20px 4px 4px;background:linear-gradient(180deg,#6f6f6f,#3a3a3a)}
.section-title{position:absolute;left:0;width:1200px;text-align:center;font-weight:700;font-size:24px;letter-spacing:.5px}

/* header */
.site-header{position:absolute;top:0;left:0;width:1200px;height:127px;background:var(--black);color:var(--white)}
.contact-label{font-size:10px;font-weight:500}
.contact-value{font-size:13px}
.brand{position:absolute;left:500px;top:28px;width:200px;display:flex;align-items:center;justify-content:center;gap:8px;font-size:14px;font-weight:700;letter-spacing:1.5px;color:var(--white)}
.brand-dot{width:22px;height:22px;border-radius:50%;background:var(--accent)}
.nav a{position:absolute;top:88px;height:24px;line-height:24px;font-size:14px;font-weight:500;color:var(--white);text-decoration:none}
.nav a.active{background:var(--accent);padding:0 12px}

/* hero */
.hero{position:absolute;top:127px;left:0;width:1200px;height:530px;background:linear-gradient(180deg,#5b86b5 0%,#8fa9c2 40%,#a58a67 70%,#5b4632 100%)}
.hero-title{position:absolute;left:700px;top:90px;font-size:52px;line-height:56px;font-weight:900;color:var(--white);text-shadow:0 2px 6px rgba(0,0,0,.35)}
.dots span{position:absolute;top:482px;width:9px;height:9px;border-radius:50%;background:var(--white)}

/* chairman */
.chairman{position:absolute;top:657px;left:0;width:1200px;height:339px;background:var(--chair-bg)}
.chairman p{position:absolute;left:165px;width:870px;text-align:center;font-size:13px;line-height:18.5px;color:var(--body)}

/* services */
.service{position:absolute;width:300px;height:255px}
.service-photo{position:absolute;left:0;top:0;width:300px;height:233px}
.service-caption{position:absolute;left:17px;top:210px;width:263px;height:45px;background:var(--white);padding:8px 0 0 18px;font-size:12px;font-weight:700;line-height:15px}
.service-caption .btn{right:16px;top:13px;width:52px;height:20px;font-size:10px}
.service-hover{position:absolute;left:17px;top:85px;width:263px;height:150px;background:var(--white);padding:16px 18px}
.service-hover h4{font-size:12px;line-height:15px}
.service-hover .rule{width:26px;height:2px;background:var(--accent);margin:8px 0 10px}
.service-hover p{font-size:11px;line-height:14px;color:var(--body)}
.service-hover .btn{right:16px;top:18px;width:52px;height:20px;font-size:10px}

/* why choose */
.why{position:absolute;top:1753px;left:0;width:1200px;height:770px;background:var(--black);color:var(--white)}
.why-photo{position:absolute;left:0;top:0;width:599px;height:770px;background:linear-gradient(180deg,#c77865 0%,#8d7c86 30%,#6d7274 55%,#3c4a33 85%,#2a3524 100%)}
.why-text{position:absolute;left:640px;width:425px;font-size:13px;line-height:19px;color:#e6e6e6}
.acc-bar{position:absolute;left:640px;width:425px;height:30px;background:var(--muted);color:var(--white);font-size:12px;padding-left:16px;line-height:30px}
.acc-bar svg{position:absolute;right:14px;top:10px}
.acc-open{background:var(--accent)}
.acc-body{position:absolute;left:640px;top:484px;width:425px;height:111px;background:var(--white);color:var(--body);padding:12px 22px;font-size:11px;line-height:15px}

/* news */
.news{position:absolute;top:2523px;left:0;width:1200px;height:573px;background:var(--news-bg)}
.news-feature{position:absolute;left:23px;top:167px;width:456px;height:346px;background:#9ca4ae;color:var(--white);padding:50px 48px}
.news-feature .date{font-size:11px;font-style:italic}
.news-feature h3{font-size:20px;line-height:26px;margin:12px 0 14px;font-weight:700}
.news-feature p{font-size:12px;line-height:17px}
.news-card{position:absolute;top:167px;width:281px;height:346px;overflow:hidden}
.news-card .head{position:absolute;left:0;top:0;width:100%;height:140px;background:#1f2b3d;color:var(--white);padding:18px 22px;font-size:16px;line-height:21px;font-weight:700}
.news-card .head .btn{position:static;display:inline-flex;width:76px;height:22px;font-size:10px;margin-top:8px}
.news-card .photo{position:absolute;left:0;top:140px;width:100%;height:206px}
.arrow-circle{position:absolute;width:32px;height:32px;border-radius:50%;background:var(--white);display:flex;align-items:center;justify-content:center}

/* projects */
.project{position:absolute;top:3270px;width:253px;height:385px;color:var(--white)}
.project h4{position:absolute;left:22px;top:22px;font-size:16px;line-height:22px;font-weight:500}
.project .vlabel{position:absolute;left:8px;bottom:60px;transform:rotate(-90deg);transform-origin:left bottom;font-size:16px;font-weight:700;white-space:nowrap;left:34px;bottom:22px}

/* drilling */
.drilling{position:absolute;top:3718px;left:0;width:1200px;height:409px;background:linear-gradient(100deg,#4a3a30 0%,#6d5443 45%,#3a2c24 100%);color:var(--white)}

/* footer */
.site-footer{position:absolute;top:4127px;left:0;width:1200px;height:415px;background:var(--footer);color:#d8d8d8}
.foot-head{position:absolute;top:75px;font-size:14px;font-weight:700;color:var(--white)}
.foot-list{position:absolute;top:117px;list-style:none;font-size:13px;line-height:23.5px}
.foot-item{position:absolute;display:flex;gap:14px;font-size:12px;line-height:17px;align-items:flex-start}
.foot-icon{flex:none;width:28px;height:28px;border-radius:50%;background:var(--white);display:flex;align-items:center;justify-content:center}
</style>
</head>
<body>

<header class="site-header">
  <svg class="abs" style="left:128px;top:30px" width="28" height="20" viewBox="0 0 28 20" fill="none" stroke="#fff" stroke-width="1.6"><rect x="1" y="1" width="26" height="18"/><path d="M1 1l13 10L27 1"/></svg>
  <div class="abs" style="left:174px;top:24px"><div class="contact-label">E MAIL US</div><div class="contact-value">info@kdrworldwide.com</div></div>
  <div class="brand"><span class="brand-dot"></span>KDR WORLDWIDE</div>
  <svg class="abs" style="left:865px;top:28px" width="28" height="28" viewBox="0 0 24 24" fill="none" stroke="#fff" stroke-width="1.5"><path d="M5 3h4l2 5-3 2a12 12 0 0 0 6 6l2-3 5 2v4a2 2 0 0 1-2 2A18 18 0 0 1 3 5a2 2 0 0 1 2-2z"/></svg>
  <div class="abs" style="left:905px;top:24px"><div class="contact-label">CALL US NOW</div><div class="contact-value" style="font-size:17px">+90 312 555 0140</div></div>
  <nav class="nav">
    <a class="active" style="left:130px">HOME</a>
    <a style="left:260px">ABOUT US</a>
    <a style="left:408px">SERVICES</a>
    <a style="left:728px">PROJECTS</a>
    <a style="left:869px">NEWS</a>
    <a style="left:970px">CONTACT US</a>
  </nav>
</header>

<section class="hero" role="img" aria-label="Drilling rig spraying water in a mountain landscape with trucks">
  <h1 class="hero-title">TRADING &amp;<br>CONTRACTING<br>SERVICES</h1>
  <div class="btn" style="left:708px;top:289px;width:135px;height:40px;font-size:16px">Read More</div>
  <div class="dots"><span style="left:550px"></span><span style="left:574px"></span><span style="left:598px"></span><span style="left:622px"></span><span style="left:646px"></span></div>
</section>

<section class="chairman">
  <div class="ornament" style="top:45px" role="img" aria-label="Decorative ornament"></div>
  <h2 class="section-title" style="top:104px">CHAIRMAN OF THE BOARD</h2>
  <p class="serif" style="top:158px">The underlying principle governing the operations of KDR Worldwide Trading Company Limited is 'Your Service Partner', the common trait enabling us to consistently deliver our value promise to our customers, partners, employees and other stakeholders. As a privately owned and diversified service company, our strength is the result of an ever-widening range of activities conducted through a number of strategic business divisions, all of which are supported by sound fiscal, management and operational expertise.</p>
  <p class="serif" style="top:251px">Today, KDR Worldwide Company is among the top highly reputed International companies and enjoys a reputation business integrity and standards of quality offer businesses and consumers alike, extraordinary services and products.</p>
</section>

<section class="services">
  <div class="ornament" style="top:1040px" role="img" aria-label="Decorative ornament"></div>
  <h2 class="section-title" style="top:1096px">OUR SERVICES</h2>

  <div class="service" style="left:130px;top:1155px">
    <div class="service-photo" role="img" aria-label="Construction workers on steel framework at sunset" style="background:linear-gradient(180deg,#6f8aa0,#c99a60 55%,#2a2a2a)"></div>
    <div class="service-caption">INFRASTRUCTURE<br>CONSTRUCTION<div class="btn">More</div></div>
  </div>
  <div class="service" style="left:450px;top:1155px">
    <div class="service-photo" role="img" aria-label="Oil refinery towers at dusk" style="background:linear-gradient(180deg,#e0a58a,#d36b4a 60%,#6a4a55)"></div>
    <div class="service-hover">
      <h4>OIL, ENEGY AND<br>GAS SERVICES</h4><div class="rule"></div>
      <p class="serif">If you are going to use a passage of Lorem Ipsum, you need to be sure there isn't anything embarrassing hidden in the middle of text.</p>
      <div class="btn">More</div>
    </div>
  </div>
  <div class="service" style="left:768px;top:1155px">
    <div class="service-photo" role="img" aria-label="Combine harvester in a wheat field" style="background:linear-gradient(180deg,#9eb7cb,#c7a36a 55%,#8a6a35)"></div>
    <div class="service-caption">AGRICULTURAL<br>PROJECTS<div class="btn">More</div></div>
  </div>

  <div class="service" style="left:130px;top:1433px">
    <div class="service-photo" role="img" aria-label="Suburban house at sunset" style="background:linear-gradient(180deg,#c25a4a,#8a6a6a 45%,#4d5258)"></div>
    <div class="service-caption">REAL ESTATE<br>DEVELOPMENT<div class="btn">More</div></div>
  </div>
  <div class="service" style="left:450px;top:1433px">
    <div class="service-photo" role="img" aria-label="Traveller in a boat on turquoise water between cliffs" style="background:linear-gradient(180deg,#5f6f5a,#2f8c8c 55%,#9b6a40)"></div>
    <div class="service-caption">TRAVEL AND<br>TOURISM<div class="btn">More</div></div>
  </div>
  <div class="service" style="left:768px;top:1433px">
    <div class="service-photo" role="img" aria-label="Food processing plant with steel tanks" style="background:linear-gradient(180deg,#8ea6c2,#b7c3cf 50%,#6e7d8e)"></div>
    <div class="service-caption">FOOD PROCESSING<br>AND TRADING<div class="btn">More</div></div>
  </div>
</section>

<section class="why">
  <div class="why-photo" role="img" aria-label="Craftsman style house with lit windows and front garden at dusk"></div>
  <div class="ornament" style="left:640px;top:32px;width:140px" role="img" aria-label="Decorative ornament"></div>
  <h2 class="abs" style="left:640px;top:82px;font-size:24px;font-weight:700">WHY CHOOSE US</h2>
  <div class="why-text" style="top:126px">KDR worlwide Supply &amp; Building</div>
  <div class="why-text" style="top:164px">KDR worlwide Supply &amp; Building provides various services. The Company offers infrastructure construction, oil, enegy and gas services, agricultural projects, real estate development, travel and tourism, and food processing and trading.</div>
  <div class="why-text" style="top:257px">Civil contracting for infrastructure, residential and heavy projects. Through its main subsidiaries; distribution of general food products, construction chemicals including corrosion inhibitors and electrical machinery; provides catering and travel agency services; ownership and operation of a school; offers human sources services including manpower supply.</div>
  <div class="why-text" style="top:388px">Drilling and Gold Mines Used Machinery, All Kinds of Construction Machinery, Drilling Machines are manufactured and sold.</div>
  <div class="acc-bar acc-open" style="top:453px">MISSION<svg width="12" height="8" viewBox="0 0 12 8" fill="none" stroke="#fff" stroke-width="1.8"><path d="M1 1l5 5 5-5"/></svg></div>
  <div class="acc-body serif">If you are going to use a passage of Lorem Ipsum, you need to be sure there isn't anything embarrassing hidden in the middle of text. All the Lorem Ipsum generators on the Internet tend to repeat predefined chunks as necessary, making this the first true generator on the Internet</div>
  <div class="acc-bar" style="top:610px">VISION<svg width="12" height="8" viewBox="0 0 12 8" fill="none" stroke="#fff" stroke-width="1.8"><path d="M1 1l5 5 5-5"/></svg></div>
  <div class="acc-bar" style="top:650px">CORE VALUES<svg width="12" height="8" viewBox="0 0 12 8" fill="none" stroke="#fff" stroke-width="1.8"><path d="M1 1l5 5 5-5"/></svg></div>
  <div class="acc-bar" style="top:692px">QUALITY<svg width="12" height="8" viewBox="0 0 12 8" fill="none" stroke="#fff" stroke-width="1.8"><path d="M1 1l5 5 5-5"/></svg></div>
</section>

<section class="news">
  <div class="ornament" style="top:42px" role="img" aria-label="Decorative ornament"></div>
  <h2 class="section-title" style="top:99px">LATEST NEWS</h2>
  <article class="news-feature">
    <div class="date serif">18 Jan,2019</div>
    <h3>CONTRARY TO POPULAR BELIEF LOREM IPSUM IS NOT SIMPLY</h3>
    <p class="serif">If you are going to use a passage of Lorem Ipsum, you need to be sure there isn't anything embarrassing hidden in the middle of text. All the Lorem Ipsum generators</p>
    <div class="btn" style="left:48px;top:265px;width:104px;height:26px;font-size:12px">Read More</div>
  </article>
  <article class="news-card" style="left:490px">
    <div class="head">CONTRARY TO POPULAR BELIEF LOREM IPSUM IS NOT SIMPLY<br><span class="btn">Read More</span></div>
    <div class="photo" role="img" aria-label="City bridge over a river at dusk" style="background:linear-gradient(180deg,#5a7aa6,#7a6a70 50%,#2a3a55)"></div>
  </article>
  <article class="news-card" style="left:778px">
    <div class="head">CONTRARY TO POPULAR BELIEF LOREM IPSUM IS NOT SIMPLY<br><span class="btn">Read More</span></div>
    <div class="photo" role="img" aria-label="Oil pump jack in a desert valley" style="background:linear-gradient(180deg,#9bb3cc,#b9a58a 55%,#7a6850)"></div>
  </article>
  <article class="news-card" style="left:1067px">
    <div class="head">CONTRARY TO POPULAR BELIEF LOREM IPSUM IS NOT SIMPLY<br><span class="btn">Read More</span></div>
    <div class="photo" role="img" aria-label="Construction crane at sunset" style="background:linear-gradient(180deg,#c9843e,#8a5a30 60%,#3a2a20)"></div>
  </article>
  <div class="arrow-circle" style="left:10px;top:325px"><svg width="10" height="14" viewBox="0 0 10 14" fill="none" stroke="#222" stroke-width="2"><path d="M8 1L2 7l6 6"/></svg></div>
  <div class="arrow-circle" style="left:1147px;top:325px"><svg width="10" height="14" viewBox="0 0 10 14" fill="none" stroke="#222" stroke-width="2"><path d="M2 1l6 6-6 6"/></svg></div>
</section>

<section class="projects">
  <div class="ornament" style="top:3140px" role="img" aria-label="Decorative ornament"></div>
  <h2 class="section-title" style="top:3196px">OUR PROJECTS</h2>
  <svg class="abs" style="left:42px;top:3455px" width="14" height="22" viewBox="0 0 14 22" fill="none" stroke="#222" stroke-width="2"><path d="M12 1L2 11l10 10"/></svg>
  <svg class="abs" style="left:1138px;top:3455px" width="14" height="22" viewBox="0 0 14 22" fill="none" stroke="#222" stroke-width="2"><path d="M2 1l10 10L2 21"/></svg>
  <div class="project" style="left:97px" role="img" aria-label="Construction workers in safety gear at a building site"><div class="abs" style="inset:0;background:linear-gradient(180deg,#6a6c70,#8a6a50 55%,#4a3a30)"></div><h4>LOREM IPSUM YOU NEED<br>TO BE SURE THERE.</h4><div class="vlabel">LOREM IPSUM</div></div>
  <div class="project" style="left:350px" role="img" aria-label="City skyline at night"><div class="abs" style="inset:0;background:linear-gradient(180deg,#2e3f5a,#4a4a55 55%,#1e2430)"></div><h4>LOREM IPSUM YOU NEED<br>TO BE SURE THERE.</h4><div class="vlabel">LOREM IPSUM</div></div>
  <div class="project" style="left:602px" role="img" aria-label="Combine harvester in a wheat field at dusk"><div class="abs" style="inset:0;background:linear-gradient(180deg,#3c4a62,#6a6070 45%,#9a7a45)"></div><h4>LOREM IPSUM YOU NEED<br>TO BE SURE THERE.</h4><div class="vlabel">LOREM IPSUM</div></div>
  <div class="project" style="left:853px" role="img" aria-label="Traveller on a beach facing green limestone islands"><div class="abs" style="inset:0;background:linear-gradient(180deg,#5a6e6a,#3d7a7a 55%,#6a5a60)"></div><h4>LOREM IPSUM YOU NEED<br>TO BE SURE THERE.</h4><div class="vlabel">LOREM IPSUM</div></div>
</section>

<section class="drilling" role="img" aria-label="Earth auger drilling into brown soil">
  <h2 class="abs" style="left:195px;top:72px;font-size:36px;line-height:46px;font-weight:700">DRILLING AND<br>GOLD MINES</h2>
  <p class="abs serif" style="left:195px;top:172px;width:440px;font-size:17px;line-height:25px">If you are going to use a passage of Lorem Ipsum, you need to be sure there isn't anything emb arrassing hidden in the middle of text.</p>
  <div class="btn" style="left:203px;top:292px;width:130px;height:36px;font-size:14px">Read More</div>
</section>

<footer class="site-footer">
  <div class="abs" style="left:135px;top:155px;width:290px;display:flex;align-items:center;justify-content:center;gap:10px;font-size:20px;font-weight:700;letter-spacing:2px;color:var(--white)"><span style="width:30px;height:30px;border-radius:50%;background:var(--accent)"></span>KDR WORLDWIDE</div>

  <div class="foot-head" style="left:492px">MENU</div>
  <ul class="foot-list" style="left:492px"><li>HOME</li><li>ABOUT US</li><li>SERVICES</li><li>PROJECTS</li><li>NEWS</li><li>CONTACT US</li></ul>

  <div class="foot-head" style="left:657px">CONTACT US</div>
  <div class="foot-item" style="left:655px;top:117px"><span class="foot-icon"><svg width="12" height="14" viewBox="0 0 12 16" fill="#151515"><path d="M6 0a6 6 0 0 0-6 6c0 4.5 6 10 6 10s6-5.5 6-10a6 6 0 0 0-6-6zm0 8.5A2.5 2.5 0 1 1 6 3.5a2.5 2.5 0 0 1 0 5z"/></svg></span><span>Meltem Sokak No: 8/4<br>Cankaya / ANKARA / TURKEY</span></div>
  <div class="foot-item" style="left:655px;top:174px"><span class="foot-icon"><svg width="13" height="13" viewBox="0 0 24 24" fill="#151515"><path d="M5 3h4l2 5-3 2a12 12 0 0 0 6 6l2-3 5 2v4a2 2 0 0 1-2 2A18 18 0 0 1 3 5a2 2 0 0 1 2-2z"/></svg></span><span>+90 312 555 0140<br>+90 312 555 0141<br>+90 312 555 0142</span></div>
  <div class="foot-item" style="left:655px;top:250px"><span class="foot-icon"><svg width="13" height="10" viewBox="0 0 14 10" fill="#151515"><path d="M0 0h14v10H0z" fill="none"/><path d="M0 0l7 5 7-5v10H0z"/></svg></span><span style="line-height:28px">info@kdrworldwide.com</span></div>

  <div class="foot-head" style="left:943px">FOLLOW US</div>
  <div class="foot-item" style="left:941px;top:117px"><span class="foot-icon"></span><span>Like us on<br>CIRCLEBOOK</span></div>
  <div class="foot-item" style="left:941px;top:178px"><span class="foot-icon"></span><span>Follow us on<br>CHIRPER</span></div>
  <div class="foot-item" style="left:941px;top:240px"><span class="foot-icon"></span><span>Follow us on<br>WORKLINK</span></div>

  <div class="abs" style="left:0;top:357px;width:1200px;height:1px;background:#262626"></div>
  <div class="abs" style="left:0;top:372px;width:1200px;text-align:center;font-size:11px;color:#bdbdbd">Copyright © 2020 All Rights Reserved</div>
</footer>

</body>
</html>
```